Oil & gas fabrication and Paint company. Need double sided with color. want original look. see attached but don't make similar!

Think Steel!

Business

```html
<!DOCTYPE html>
<html lang="en">
<head>
<meta charset="utf-8">
<title>Kestrel Fabrication &amp; Paint — Business Card</title>
<link href="https://fonts.googleapis.com/css2?family=Open+Sans:wght@400;700&family=Great+Vibes&display=swap" rel="stylesheet">
<style>
  :root{
    --page:#e8e4de;
    --ink:#0b0b0c;
    --white:#f4f1ea;
    --gold:#f3b81f;
    --amber:#e58a12;
    --ember:#a8410d;
    --rust:#5e1e0a;
    --badge:#2f3a8f;
  }
  *{box-sizing:border-box;margin:0;padding:0}
  html,body{width:704px;height:1200px;overflow:hidden}
  body{background:var(--page);font-family:"Open Sans",Arial,sans-serif;position:relative}

  .card{position:absolute;left:42px;width:620px;height:354px;border-radius:4px;overflow:hidden;
        background:var(--ink);box-shadow:0 10px 24px rgba(0,0,0,.25)}
  .card--front{top:170px}
  .card--back{top:676px}

  .sunset-photo{position:absolute;inset:0;
    background:linear-gradient(180deg,var(--rust) 0%,var(--ember) 14%,var(--amber) 34%,var(--gold) 50%,var(--amber) 62%,#3a1606 78%,var(--ink) 92%)}

  .brand{position:absolute;display:flex;align-items:center;gap:12px}
  .brand__dot{width:34px;height:34px;border-radius:50%;background:var(--badge)}
  .brand__name{font-weight:700;font-size:30px;letter-spacing:2px;color:var(--white);line-height:1}
  .brand__sub{display:block;font-weight:400;font-size:11px;letter-spacing:1px;color:var(--white);margin-top:4px}
  .card--front .brand{left:40px;top:128px}

  .tagline{position:absolute;right:38px;bottom:30px;font-family:"Great Vibes",cursive;
    font-size:46px;color:var(--white)}

  .back-photo{position:absolute;right:0;top:0;width:52%;height:100%;
    background:linear-gradient(200deg,var(--ember) 0%,var(--amber) 30%,var(--gold) 48%,#7a3008 72%,var(--ink) 100%)}
  .back-shade{position:absolute;right:0;top:0;width:52%;height:100%;
    background:linear-gradient(90deg,var(--ink) 0%,rgba(11,11,12,0) 45%)}

  .call{position:absolute;right:36px;top:44px;text-align:left}
  .call__label{display:flex;align-items:center;gap:8px;color:var(--white);font-weight:700;font-size:22px}
  .call__number{color:var(--gold);font-weight:700;font-size:24px;margin-top:2px}

  .card--back .brand{left:32px;top:40px}
  .holder{position:absolute;left:32px;top:130px;color:var(--gold);font-weight:700;font-size:18px}
  .contacts{position:absolute;left:32px;top:162px;list-style:none}
  .contacts li{display:flex;align-items:center;gap:10px;color:var(--white);font-size:13px;line-height:20px}
  .contacts .ic{width:10px;height:10px;background:var(--amber);border-radius:1px;flex:none}
  .address{position:absolute;left:32px;top:272px;color:var(--gold);font-size:13px;line-height:19px}
</style>
</head>
<body>

<section class="card card--front" aria-label="Card front">
  <div class="sunset-photo" role="img" aria-label="Photo of an offshore rig and crane silhouetted against an orange sunset sky"></div>
  <div class="brand">
    <span class="brand__dot"></span>
    <span class="brand__name">KESTREL<span class="brand__sub">Fabrication &amp; Paint</span></span>
  </div>
  <p class="tagline">It's a way of life !</p>
</section>

<section class="card card--back" aria-label="Card back">
  <div class="back-photo" role="img" aria-label="Photo of an orange sunset sky over an offshore rig silhouette"></div>
  <div class="back-shade"></div>

  <div class="call">
    <div class="call__label">
      <svg width="20" height="18" viewBox="0 0 20 18" aria-hidden="true">
        <path d="M2 5c0-2 2-3 8-3s8 1 8 3v2h-4V5H6v2H2z" fill="var(--white)"/>
        <rect x="4" y="8" width="12" height="9" rx="1.5" fill="var(--white)"/>
        <circle cx="10" cy="12.5" r="2" fill="var(--ink)"/>
      </svg>
      CALL
    </div>
    <div class="call__number">1-877-2-RIG-FAB</div>
  </div>

  <div class="brand">
    <span class="brand__dot"></span>
    <span class="brand__name">KESTREL<span class="brand__sub">Fabrication &amp; Paint</span></span>
  </div>

  <p class="holder">Dana Merrow</p>
  <ul class="contacts">
    <li><span class="ic"></span>0100 555 010</li>
    <li><span class="ic"></span>0100 555 011</li>
    <li><span class="ic"></span>0100 555 012</li>
    <li><span class="ic"></span>youremail@email.com</li>
    <li><span class="ic"></span>www.yourwebsite.com</li>
  </ul>
  <p class="address">Your address can put here<br>your address can put here</p>
</section>

</body>
</html>
```